FotoVELD buisnesscard

Hey :) I need a modern buisnesscard for my company FotoVELD
It most have:
Dagligleder og Fotograf: Eirik Tobias Vangsnes

Mob: +4791642508
Epost: post@fotoveld-eks.no
Adresse: Bjørkeveien22, 7190 Fjellvik

Facbook and instagram logo with text FotoVELD

FotoVELD logo

It Company

```html
<!DOCTYPE html>
<html lang="no">
<head>
<meta charset="utf-8">
<title>FotoVELD – visittkort</title>
<link rel="stylesheet" href="https://fonts.googleapis.com/css2?family=Montserrat:wght@400;500;600;800&display=swap">
<style>
  :root {
    --bg: #2b2b2b;
    --card: #000000;
    --silver: #b5b5b5;
    --silver-light: #d6d6d6;
    --white: #ffffff;
    --text: #c9c9c9;
    --divider: #777777;
  }
  * { margin: 0; padding: 0; box-sizing: border-box; }
  html, body { width: 1200px; height: 900px; overflow: hidden; background: var(--bg); }
  body { position: relative; font-family: "Montserrat", sans-serif; color: var(--text); }

  .card {
    position: absolute;
    width: 620px;
    height: 354px;
    background: var(--card);
    border-radius: 18px;
    overflow: hidden;
  }
  .card--front { left: 110px; top: 60px; }
  .card--back  { left: 470px; top: 486px; }

  /* bottom stepped stripe */
  .stripe { position: absolute; left: 0; right: 0; bottom: 0; height: 26px; }
  .stripe__end-left  { position: absolute; left: 0; bottom: 0; width: 80px; height: 9px; background: var(--white); }
  .stripe__bar       { position: absolute; left: 86px; right: 86px; bottom: 0; height: 18px; background: var(--silver); }
  .stripe__end-right { position: absolute; right: 0; bottom: 12px; width: 80px; height: 9px; background: var(--white); }

  /* front */
  .brand-mark {
    position: absolute; left: 0; right: 0; top: 120px;
    text-align: center;
    font-weight: 800; font-size: 64px; letter-spacing: 1px;
    color: var(--silver);
  }
  .social {
    position: absolute; right: 20px; bottom: 46px;
    display: flex; flex-direction: column; align-items: flex-end; gap: 6px;
    font-size: 13px; font-weight: 500; color: var(--text);
  }
  .social__square { width: 12px; height: 12px; background: var(--silver); }

  /* back */
  .brand-name {
    position: absolute; left: 0; right: 0; top: 78px;
    text-align: center;
    font-weight: 800; font-size: 54px; letter-spacing: 0.5px;
    color: var(--silver);
  }
  .details {
    position: absolute; left: 0; right: 0; top: 196px;
    display: flex; justify-content: center; align-items: stretch; gap: 16px;
  }
  .person { text-align: right; display: flex; flex-direction: column; justify-content: center; }
  .person__name  { font-size: 20px; font-weight: 600; color: var(--silver-light); letter-spacing: 0.5px; }
  .person__title { font-size: 15px; font-weight: 400; color: var(--text); margin-top: 2px; }
  .divider { width: 1px; background: var(--divider); }
  .contact { list-style: none; display: flex; flex-direction: column; gap: 4px; justify-content: center; }
  .contact__item { display: flex; align-items: center; gap: 8px; font-size: 13.5px; color: var(--text); white-space: nowrap; }
  .contact__icon { width: 11px; height: 11px; fill: var(--text); flex: none; }
</style>
</head>
<body>

<section class="card card--front" aria-label="Kortets forside">
  <div class="brand-mark">FotoVELD</div>
  <div class="social">
    <span class="social__square"></span>
    <span class="social__name">FotoVELD</span>
  </div>
  <div class="stripe">
    <span class="stripe__end-left"></span>
    <span class="stripe__bar"></span>
    <span class="stripe__end-right"></span>
  </div>
</section>

<section class="card card--back" aria-label="Kortets bakside">
  <div class="brand-name">FotoVELD</div>
  <div class="details">
    <div class="person">
      <p class="person__name">Eirik Tobias Vangsnes</p>
      <p class="person__title">Dagligleder og Fotograf</p>
    </div>
    <span class="divider"></span>
    <ul class="contact">
      <li class="contact__item">
        <svg class="contact__icon" viewBox="0 0 24 24"><path d="M6.6 10.8a15 15 0 0 0 6.6 6.6l2.2-2.2c.3-.3.7-.4 1-.2 1.1.4 2.3.6 3.6.6.6 0 1 .4 1 1V20c0 .6-.4 1-1 1A17 17 0 0 1 3 4c0-.6.4-1 1-1h3.5c.6 0 1 .4 1 1 0 1.3.2 2.5.6 3.6.1.3 0 .7-.2 1z"/></svg>
        +4791642508
      </li>
      <li class="contact__item">
        <svg class="contact__icon" viewBox="0 0 24 24"><path d="M2 5h20v14H2zm2 2v.5l8 5 8-5V7zm0 2.8V17h16V9.8l-8 5z"/></svg>
        post@fotoveld-eks.no
      </li>
      <li class="contact__item">
        <svg class="contact__icon" viewBox="0 0 24 24"><path d="M12 2a7 7 0 0 0-7 7c0 5 7 13 7 13s7-8 7-13a7 7 0 0 0-7-7zm0 9.5A2.5 2.5 0 1 1 12 6.5a2.5 2.5 0 0 1 0 5z"/></svg>
        Bjørkeveien22, 7190 Fjellvik
      </li>
    </ul>
  </div>
  <div class="stripe">
    <span class="stripe__end-left"></span>
    <span class="stripe__bar"></span>
    <span class="stripe__end-right"></span>
  </div>
</section>

</body>
</html>
```